Tervolan Pty Ltd professional business card

A professional business card template using the colours from the supplied logo.
Clean crisp lines while, Modern while not being over the top.

Target Market(s)

Construction, commerical and industrial

Industry/Entity Type

Communications

Contact Information for Business Card

For a Communications, IT, Optical fibre installation company

Colors
37b8a4

```html
<!DOCTYPE html>
<html lang="en">
<head>
<meta charset="utf-8">
<title>Tervolan Pty Ltd – Business Card</title>
<link href="https://fonts.googleapis.com/css2?family=Jost:wght@300;400;600&display=swap" rel="stylesheet">
<style>
  :root {
    --teal: #37b8a4;
    --grey: #6e6f71;
    --paper: #fbfbfa;
    --backdrop: #e4e4e2;
    --ink-light: #ffffff;
  }
  * { box-sizing: border-box; margin: 0; padding: 0; }
  html, body {
    width: 1200px; height: 801px; overflow: hidden;
    background: var(--backdrop);
    font-family: 'Jost', sans-serif;
  }
  .stage {
    width: 1200px; height: 801px;
    display: flex; align-items: center; justify-content: center; gap: 40px;
  }
  .card {
    position: relative;
    width: 525px; height: 300px;
    background: var(--paper);
    box-shadow: 0 2px 10px rgba(0,0,0,0.12);
  }
  .wordmark {
    font-family: 'Jost', sans-serif;
    font-weight: 600;
    color: var(--grey);
    letter-spacing: 1px;
    line-height: 1;
    display: flex; align-items: center; gap: 12px;
  }
  .wordmark-square {
    display: inline-block;
    background: var(--teal);
  }
  .card-front .wordmark {
    position: absolute; left: 40px; top: 48px;
    font-size: 44px;
  }
  .card-front .wordmark-square { width: 30px; height: 30px; }
  .name-block {
    position: absolute; left: 40px; bottom: 46px;
  }
  .name-band {
    display: inline-block;
    background: var(--teal);
    color: var(--ink-light);
    font-weight: 400;
    font-size: 19px;
    letter-spacing: 1.5px;
    text-transform: uppercase;
    padding: 4px 12px 4px 10px;
  }
  .title-band {
    display: block;
    width: fit-content;
    margin-left: 28px;
    background: var(--grey);
    color: #e3e3e3;
    font-weight: 300;
    font-size: 14px;
    letter-spacing: 1px;
    padding: 3px 12px;
  }
  .contact-list {
    position: absolute; right: 30px; bottom: 44px;
    list-style: none;
    text-align: right;
  }
  .contact-item {
    display: flex; align-items: center; justify-content: flex-end; gap: 8px;
    font-weight: 300;
    font-size: 14px;
    color: var(--grey);
    letter-spacing: 1px;
    line-height: 22px;
  }
  .contact-item .accent { color: var(--teal); }
  .contact-icon { width: 16px; height: 16px; flex: none; }
  .card-back {
    display: flex; align-items: center; justify-content: center;
  }
  .card-back .wordmark { font-size: 56px; gap: 16px; }
  .card-back .wordmark-square { width: 38px; height: 38px; }
</style>
</head>
<body>
<main class="stage">
  <section class="card card-front" aria-label="Business card front">
    <div class="wordmark"><span class="wordmark-square"></span>TERVOLAN</div>

    <div class="name-block">
      <span class="name-band">Daniel Harrow</span>
      <span class="title-band">Managing Director</span>
    </div>

    <ul class="contact-list">
      <li class="contact-item">000 000 00 00
        <svg class="contact-icon" viewBox="0 0 16 16" aria-hidden="true">
          <circle cx="8" cy="8" r="8" fill="var(--teal)"/>
          <path d="M5.2 4.2 L6.6 4 L7.3 5.8 L6.4 6.5 Q7.2 8.4 9.4 9.6 L10.1 8.7 L11.9 9.4 L11.7 10.8 Q8.8 11.5 6.5 9.2 Q4.4 7 5.2 4.2 Z" fill="#fff"/>
        </svg>
      </li>
      <li class="contact-item">info@tervolan.com
        <svg class="contact-icon" viewBox="0 0 16 16" aria-hidden="true">
          <circle cx="8" cy="8" r="8" fill="var(--teal)"/>
          <rect x="4" y="5" width="8" height="6" fill="none" stroke="#fff" stroke-width="1"/>
          <path d="M4 5 L8 8.3 L12 5" fill="none" stroke="#fff" stroke-width="1"/>
        </svg>
      </li>
      <li class="contact-item"><span>www.<span class="accent">tervolan</span>.com</span>
        <svg class="contact-icon" viewBox="0 0 16 16" aria-hidden="true">
          <circle cx="8" cy="8" r="8" fill="var(--teal)"/>
          <circle cx="8" cy="8" r="4" fill="none" stroke="#fff" stroke-width="1"/>
          <ellipse cx="8" cy="8" rx="1.7" ry="4" fill="none" stroke="#fff" stroke-width="0.9"/>
          <line x1="4" y1="8" x2="12" y2="8" stroke="#fff" stroke-width="0.9"/>
        </svg>
      </li>
    </ul>
  </section>

  <section class="card card-back" aria-label="Business card back">
    <div class="wordmark"><span class="wordmark-square"></span>TERVOLAN</div>
  </section>
</main>
</body>
</html>
```